Kovalen Spinal Care and Performance

We need new business cards, something more modern, clean. On the back of the card maybe a quote. The Dr. likes, “The doctor of the future will give no medicine, but will interest his patient in the care of the human frame, in diet and in the cause and prevention of disease.” - Walter Brisby. We are open to other suggestions. We are a chiropractic office.

```html
<!DOCTYPE html>
<html lang="en">
<head>
<meta charset="UTF-8">
<title>Kovalen Chiropractic Studio — Business Card</title>
<link rel="stylesheet" href="https://fonts.googleapis.com/css2?family=Open+Sans:wght@400;600;700&display=swap">
<style>
  :root {
    --backdrop: #2b2b2b;
    --purple: #7e4389;
    --purple-light: #8b4b97;
    --purple-dark: #743d81;
    --green: #9bc424;
    --ink: #2a2a2a;
    --card-white: #ffffff;
    --card-grey: #ececec;
  }
  * { box-sizing: border-box; margin: 0; padding: 0; }
  html, body {
    width: 1200px; height: 1200px; overflow: hidden;
    background: var(--backdrop);
    font-family: "Open Sans", sans-serif;
  }
  .sheet {
    width: 1200px; height: 1200px;
    display: flex; flex-direction: column;
    align-items: center; justify-content: center; gap: 50px;
  }
  .card {
    width: 880px; height: 500px;
    border-radius: 36px;
    position: relative;
    overflow: hidden;
    box-shadow: 0 14px 36px rgba(0,0,0,0.45);
  }
  .card--front {
    background: linear-gradient(160deg, var(--purple-light), var(--purple-dark));
    display: flex; align-items: center; justify-content: center;
  }
  .brand {
    display: flex; align-items: center; gap: 16px;
    font-weight: 600; color: var(--card-white);
    font-size: 44px; letter-spacing: 0.5px; white-space: nowrap;
  }
  .brand__dot {
    width: 22px; height: 22px; border-radius: 50%;
    background: var(--green);
    flex: none;
  }
  .card--back {
    background: linear-gradient(180deg, var(--card-white) 40%, var(--card-grey));
  }
  .card--back .brand {
    position: absolute; top: 60px; right: 60px;
    color: var(--purple); font-size: 28px; gap: 12px;
  }
  .card--back .brand__dot { width: 16px; height: 16px; }
  .identity {
    position: absolute; left: 120px; top: 240px; width: 300px;
    text-align: right;
  }
  .identity__name {
    font-weight: 700; font-size: 44px; color: var(--ink); line-height: 1.1;
  }
  .identity__role {
    font-weight: 400; font-size: 30px; color: var(--purple); line-height: 1.2;
  }
  .divider {
    position: absolute; left: 460px; top: 190px;
    width: 2px; height: 220px; background: var(--green);
  }
  .contacts {
    position: absolute; left: 500px; top: 200px;
    list-style: none; color: var(--ink);
    font-size: 23px; line-height: 1.3;
  }
  .contacts li {
    display: flex; align-items: flex-start; gap: 14px; margin-bottom: 10px;
  }
  .contacts svg {
    width: 24px; height: 24px; flex: none; margin-top: 3px;
    fill: var(--purple);
  }
</style>
</head>
<body>
<main class="sheet">
  <section class="card card--front" aria-label="Card front">
    <div class="brand"><span class="brand__dot"></span>Kovalen Chiropractic Studio</div>
  </section>

  <section class="card card--back" aria-label="Card back">
    <div class="brand"><span class="brand__dot"></span>Kovalen Chiropractic Studio</div>

    <div class="identity">
      <p class="identity__name">Your Name</p>
      <p class="identity__role">Director</p>
    </div>

    <div class="divider"></div>

    <ul class="contacts">
      <li>
        <svg viewBox="0 0 24 24" aria-hidden="true"><path d="M12 2a7 7 0 0 0-7 7c0 5 7 13 7 13s7-8 7-13a7 7 0 0 0-7-7zm0 9.5A2.5 2.5 0 1 1 12 6.5a2.5 2.5 0 0 1 0 5z"/></svg>
        <span>2364 First Address Line<br>Second Address Line, 56324</span>
      </li>
      <li>
        <svg viewBox="0 0 24 24" aria-hidden="true"><path d="M6.6 10.8a15.1 15.1 0 0 0 6.6 6.6l2.2-2.2a1 1 0 0 1 1-.25 11.4 11.4 0 0 0 3.6.57 1 1 0 0 1 1 1V20a1 1 0 0 1-1 1A17 17 0 0 1 3 4a1 1 0 0 1 1-1h3.5a1 1 0 0 1 1 1c0 1.25.2 2.45.57 3.57a1 1 0 0 1-.25 1z"/></svg>
        <span>+0123 456 7899</span>
      </li>
      <li>
        <svg viewBox="0 0 24 24" aria-hidden="true"><path d="M3 5h18a1 1 0 0 1 1 1v12a1 1 0 0 1-1 1H3a1 1 0 0 1-1-1V6a1 1 0 0 1 1-1zm1 2.2V17h16V7.2l-8 5.3z"/></svg>
        <span>youremail@email.com</span>
      </li>
      <li>
        <svg viewBox="0 0 24 24" aria-hidden="true"><path d="M12 2a10 10 0 1 0 0 20 10 10 0 0 0 0-20zm6.9 9h-3a15 15 0 0 0-1.3-5.6A8 8 0 0 1 18.9 11zM12 4.1c.9 1.2 1.7 3.6 1.900 6.9h-3.8c.2-3.3 1-5.7 1.9-6.9zM9.4 5.4A15 15 0 0 0 8.1 11h-3a8 8 0 0 1 4.3-5.6zM5.1 13h3a15 15 0 0 0 1.3 5.6A8 8 0 0 1 5.1 13zm6.9 6.9c-.9-1.2-1.7-3.6-1.9-6.9h3.8c-.2 3.3-1 5.7-1.9 6.9zm2.6-1.3a15 15 0 0 0 1.3-5.6h3a8 8 0 0 1-4.3 5.6z"/></svg>
        <span>yourwebsite.com</span>
      </li>
    </ul>
  </section>
</main>
</body>
</html>
```